Pivots & Treads .com

This website is simple!!!
Landing page background image should capture the customers attention!!! We will provide a image as a example of what we like. The purpose for this website is to provide customers with a clean easy way to request a quote for industrial casters and wheels by OEM’s as well as maintenance departments worldwide. Please see if you can follow our thought process below.
Customer comes to website, they are invited to Request a Quote by providing us with Manufacturer Name, Manufacturers Part # and quantity needed.
If this is not known the customer will complete will WP conversation format form answering about 10 questions
Or
Look up the part number in one of the 8 to 12 catalogs located in the Flippin Book format on our catalog page, or equal plug in .
When the client request a quote a account page will pop up request The following:
Clients first and last name
Email address
And optional questions
Company name and best contact number.
Once this is complete customer will hit SUBMIT.
The customers request will be in system. A email will be sent to Customer service notifying us the Quote Request has been made.
We will then build a quote for the customer with a good, better and best options. Customers Request a Quote submission may have more than one caster or wheel requested at a time, so website must allow this.
When the customer comes back into website there email address will come up as the account name and request a password be made for them. This will allow them to store quotes in their account for future needs. If quote is older than 30 day the system will trigger a button at the bottom of the quote for resubmit Request for updated quote.
Once customer reviews quote the quote can be Converted to order within the website.
Once Converted the system will send us a email and order will be processed.
We will need a Chat program that will text to CS the questions.
You will need to have high quality graphic design skills on your team.
We have found 2 plugins that would work nicely with our new website Flippin books to showcase our catalogs for customers to research and WPForms conversation forms to complete request for quote form.
Just Ideas:
Very very ghosted caster blueprint in white background but very very ghosted or the icon just idea
We have never had a font used we like
Grayscale every except for rubber on wheels and logo icon
Website should have hamburger menu on left
Website should hav responsive deign
Account head on right side
Has anyone read the brief from top to bottom and the updates, I’m seeing a lot of duplicates of the website I posted in images I want a clean website With lite backgrand with the poly being definite colors on each wheel I added a green yellow and red image has anyone looked at that Just a question?
Went on vacation/holiday

```html
<!DOCTYPE html>
<html lang="en">
<head>
<meta charset="utf-8">
<title>Pivots &amp; Treads — Home Page and Quote Form</title>
<link rel="stylesheet" href="https://fonts.googleapis.com/css2?family=Montserrat:wght@500;700;800&family=Poppins:wght@400;500;600;700&display=swap">
<style>
  :root{
    --board:#dedfe0;
    --brand-blue:#284596;
    --brand-blue-dark:#1f3a86;
    --ink:#1b1c1e;
    --charcoal:#3a3d42;
    --charcoal-light:#55595e;
    --field:#ececec;
    --muted:#5b5e63;
    --footer-text:#a3a6ab;
    --white:#ffffff;
  }
  *{box-sizing:border-box;margin:0;padding:0}
  html,body{width:846px;height:1200px;overflow:hidden;background:var(--board)}
  body{position:relative;font-family:"Poppins",sans-serif;color:var(--ink)}
  .icon-defs{position:absolute;width:0;height:0;overflow:hidden}

  .section-title{
    position:absolute;left:0;width:846px;text-align:center;
    font-family:"Montserrat",sans-serif;font-weight:700;font-size:19.5px;
    letter-spacing:.06em;color:var(--brand-blue);
  }
  .section-title--home{top:26px}
  .section-title--form{top:623px}

  .frame{
    position:absolute;left:37px;width:765px;height:490px;overflow:hidden;
    background:var(--white);box-shadow:0 12px 26px rgba(0,0,0,.16);
  }
  .frame--home{top:68px}
  .frame--form{top:665px}

  /* header */
  .site-header{position:absolute;left:0;top:0;width:765px;height:66px;background:var(--white)}
  .topbar-shape{position:absolute;left:0;top:0}
  .contact{
    position:absolute;top:0;height:26px;display:flex;align-items:center;gap:6px;
    font-size:10px;color:var(--white);font-weight:400;letter-spacing:.01em;
  }
  .contact svg{width:10px;height:10px;fill:var(--white)}
  .contact--phone{left:443px}
  .contact--email{left:567px}
  .contact-divider{position:absolute;left:548px;top:7px;width:1px;height:12px;background:#8a8d92}
  .brand{
    position:absolute;left:52px;top:23px;display:flex;align-items:center;gap:8px;
    font-family:"Poppins",sans-serif;font-weight:600;font-size:15px;color:var(--brand-blue);
    letter-spacing:.01em;
  }
  .brand-dot{width:22px;height:22px;border-radius:50%;background:var(--brand-blue)}
  .menu-toggle{
    position:absolute;left:653px;top:39px;display:flex;align-items:center;gap:6px;
    font-family:"Poppins",sans-serif;font-weight:700;font-size:9.5px;letter-spacing:.03em;color:var(--ink);
  }
  .menu-toggle .bars{display:flex;flex-direction:column;gap:3px}
  .menu-toggle .bars span{display:block;width:16px;height:1.6px;background:var(--ink)}

  /* hero */
  .hero{
    position:absolute;left:0;top:66px;width:765px;height:368px;
    background:radial-gradient(ellipse at 45% 40%,#f6f6f6 0%,#e9e9e9 45%,#d2d2d2 100%);
  }
  .hero-photo{
    position:absolute;left:372px;top:72px;width:343px;height:235px;
    background:radial-gradient(ellipse at 50% 52%,rgba(74,104,165,.38) 0%,rgba(160,170,188,.42) 38%,rgba(205,208,214,.35) 58%,rgba(230,230,230,0) 74%);
  }
  .hero-eyebrow{
    position:absolute;left:51px;top:62px;display:flex;align-items:center;gap:8px;
    font-family:"Montserrat",sans-serif;font-weight:500;font-size:16.5px;letter-spacing:.01em;
  }
  .hero-eyebrow .rule{position:relative;width:28px;height:1.4px;background:var(--ink)}
  .hero-eyebrow .rule::after{content:"";position:absolute;right:0;top:-3px;width:1.4px;height:7.5px;background:var(--ink)}
  .hero-title{
    position:absolute;left:49px;top:80px;
    font-family:"Montserrat",sans-serif;font-weight:800;font-size:41px;line-height:46px;
    letter-spacing:-.005em;color:var(--ink);
  }
  .steps{position:absolute;left:51px;top:174px;display:flex;align-items:center;height:28px}
  .steps-label{font-size:13px;font-weight:400;margin-right:10px;letter-spacing:.02em}
  .step-track{position:relative;display:flex;align-items:center;gap:7px}
  .step-track::before{content:"";position:absolute;left:10px;right:10px;top:13.5px;height:1.5px;background:#b8babd}
  .step{
    position:relative;width:27px;height:27px;border-radius:50%;background:var(--white);
    box-shadow:0 1px 4px rgba(0,0,0,.18);display:flex;align-items:center;justify-content:center;
    font-family:"Montserrat",sans-serif;font-weight:700;font-size:12px;
  }
  .bullet-list{position:absolute;left:51px;top:215px;list-style:none;width:260px;display:flex;flex-wrap:wrap;column-gap:10px;row-gap:8px}
  .bullet-list li{display:flex;align-items:center;gap:5px;font-size:12px;line-height:18px;letter-spacing:.01em}
  .bullet-list svg{width:11px;height:11px}
  .btn{
    position:absolute;height:32px;border-radius:16px;display:flex;align-items:center;justify-content:center;gap:6px;
    font-family:"Poppins",sans-serif;font-weight:700;font-size:9.5px;letter-spacing:.06em;color:var(--white);
  }
  .btn svg{width:9px;height:9px;fill:var(--white)}
  .btn--quote{left:51px;top:275px;width:152px;background:var(--brand-blue)}
  .btn--catalog{left:214px;top:275px;width:111px;background:var(--charcoal)}
  .btn--catalog svg{width:11px;height:10px}

  /* footer */
  .site-footer{position:absolute;left:0;top:400px;width:765px;height:90px}
  .footer-shape{position:absolute;left:0;top:0}
  .copyright{
    position:absolute;left:0;top:54px;width:765px;text-align:center;
    font-size:10.5px;color:var(--footer-text);letter-spacing:.01em;
  }

  /* modal state */
  .dim{position:absolute;inset:0;background:rgba(8,8,10,.86)}
  .quote-modal{
    position:absolute;left:129px;top:101px;width:509px;height:286px;
    border:8.5px solid var(--brand-blue);background:var(--white);
  }
  .modal-close{
    position:absolute;right:10px;top:8px;display:flex;align-items:center;gap:5px;
    font-family:"Poppins",sans-serif;font-weight:700;font-size:9.5px;letter-spacing:.07em;
  }
  .modal-close svg{width:9px;height:9px;stroke:var(--ink);stroke-width:2.2}
  .quote-fields{
    position:absolute;left:31px;top:51px;display:grid;grid-template-columns:210px 210px;
    column-gap:11px;row-gap:10.5px;
  }
  .field{
    height:32px;border-radius:6px;background:var(--field);display:flex;align-items:center;gap:7px;
    padding-left:11px;font-size:10px;color:var(--muted);letter-spacing:.01em;
  }
  .field svg{width:10px;height:10px;fill:#6a6d72}
  .btn--submit{left:174.5px;top:186.5px;width:143px;background:var(--brand-blue)}
</style>
</head>
<body>

<svg class="icon-defs" aria-hidden="true">
  <symbol id="i-arrow" viewBox="0 0 16 16"><path d="M8.6 2.2 7.2 3.6 10.6 7H1.5v2h9.1l-3.4 3.4 1.4 1.4L14.4 8z"/></symbol>
  <symbol id="i-phone" viewBox="0 0 16 16"><path d="M3.6 1h2.6l1.2 3.4-1.7 1.3a9 9 0 0 0 4.6 4.6l1.3-1.7 3.4 1.2v2.6c0 .9-.7 1.6-1.6 1.6C6.9 14 2 9.1 2 2.6 2 1.7 2.7 1 3.6 1z"/></symbol>
  <symbol id="i-mail-open" viewBox="0 0 16 16"><path d="M8 1 1 5.5V15h14V5.5zm0 2.3 4.8 3.1L8 9.6 3.2 6.4z"/></symbol>
  <symbol id="i-mail" viewBox="0 0 16 16"><path d="M1 3h14v1.6L8 9 1 4.6zm0 3.4 7 4.4 7-4.4V13H1z"/></symbol>
  <symbol id="i-user" viewBox="0 0 16 16"><circle cx="8" cy="4.5" r="3.5"/><path d="M1.5 15c0-3.6 2.9-6 6.5-6s6.5 2.4 6.5 6z"/></symbol>
  <symbol id="i-question" viewBox="0 0 16 16"><path d="M8 1C5.6 1 4 2.5 4 4.7h2.3c0-1 .7-1.6 1.7-1.6s1.6.6 1.6 1.4c0 1.9-2.8 1.8-2.8 4.9h2.3c0-2.3 2.9-2.4 2.9-5C12 2.3 10.3 1 8 1zM6.9 12h2.4v2.6H6.9z"/></symbol>
  <symbol id="i-briefcase" viewBox="0 0 16 16"><path d="M6 1.5h4A1.5 1.5 0 0 1 11.5 3v1H15v4.5H1V4h3.5V3A1.5 1.5 0 0 1 6 1.5zm0 1.5v1h4V3zM1 9.5h6V11h2V9.5h6V15H1z"/></symbol>
  <symbol id="i-book" viewBox="0 0 18 16"><path d="M1 2c2.6-.6 5 0 7.2 1.4V15C6 13.7 3.6 13.2 1 13.7zm16 0v11.7c-2.6-.5-5 0-7.2 1.3V3.4C12 2 14.4 1.4 17 2z"/></symbol>
  <symbol id="i-arrow-circle" viewBox="0 0 16 16"><circle cx="8" cy="8" r="7.5" fill="#1b1c1e"/><path fill="#fff" d="M8.3 4.2 7.2 5.3 9.1 7.2H4.2v1.6h4.9l-1.9 1.9 1.1 1.1L12.1 8z"/></symbol>
  <symbol id="i-close" viewBox="0 0 10 10"><path d="M1 1l8 8M9 1 1 9" fill="none"/></symbol>
</svg>

<h2 class="section-title section-title--home">HOME PAGE</h2>

<section class="frame frame--home">
  <header class="site-header">
    <svg class="topbar-shape" width="765" height="27" viewBox="0 0 765 27" aria-hidden="true">
      <polygon points="328,0 765,0 765,26 428,26 421,3 332,3" fill="#3a3d42"/>
    </svg>
    <span class="contact contact--phone"><svg><use href="#i-phone"/></svg>123-456-7890</span>
    <span class="contact-divider"></span>
    <span class="contact contact--email"><svg><use href="#i-mail-open"/></svg>hello@pivotstreads.com</span>
    <div class="brand"><span class="brand-dot"></span>PIVOTS &amp; TREADS.com</div>
    <div class="menu-toggle">MENU <span class="bars"><span></span><span></span><span></span></span></div>
  </header>

  <div class="hero">
    <div class="hero-photo" role="img" aria-label="Photo of two chrome swivel casters with blue polyurethane wheels"></div>
    <p class="hero-eyebrow">SOLUTIONS FOR <span class="rule"></span></p>
    <h1 class="hero-title">ALL YOUR<br>APPLICATIONS</h1>
    <div class="steps">
      <span class="steps-label">Easy as :</span>
      <div class="step-track"><span class="step">1</span><span class="step">2</span><span class="step">3</span></div>
    </div>
    <ul class="bullet-list">
      <li><svg><use href="#i-arrow-circle"/></svg>Request a Quote</li>
      <li><svg><use href="#i-arrow-circle"/></svg>Receive a Quote</li>
      <li><svg><use href="#i-arrow-circle"/></svg>Convert a Quote to order</li>
    </ul>
    <span class="btn btn--quote">REQUEST A QUOTE <svg><use href="#i-arrow"/></svg></span>
    <span class="btn btn--catalog">CATALOG <svg viewBox="0 0 18 16"><use href="#i-book"/></svg></span>
  </div>

  <footer class="site-footer">
    <svg class="footer-shape" width="765" height="90" viewBox="0 0 765 90" aria-hidden="true">
      <polygon points="0,34 142,34 142,45 78,45 60,22 0,22" fill="#55595e"/>
      <polygon points="765,34 623,34 623,45 687,45 705,22 765,22" fill="#55595e"/>
      <polygon points="0,11 64,11 82,34 683,34 701,11 765,11 765,90 0,90" fill="#3a3d42"/>
    </svg>
    <p class="copyright">Copyright © 2022 Pivots &amp; Treads All rights reserved.</p>
  </footer>
</section>

<h2 class="section-title section-title--form">HOME PAGE REQUEST A QUOTE POP UP FORM</h2>

<section class="frame frame--form">
  <header class="site-header">
    <svg class="topbar-shape" width="765" height="27" viewBox="0 0 765 27" aria-hidden="true">
      <polygon points="328,0 765,0 765,26 428,26 421,3 332,3" fill="#3a3d42"/>
    </svg>
    <span class="contact contact--phone"><svg><use href="#i-phone"/></svg>123-456-7890</span>
    <span class="contact-divider"></span>
    <span class="contact contact--email"><svg><use href="#i-mail-open"/></svg>hello@pivotstreads.com</span>
    <div class="brand"><span class="brand-dot"></span>PIVOTS &amp; TREADS.com</div>
    <div class="menu-toggle">MENU <span class="bars"><span></span><span></span><span></span></span></div>
  </header>

  <div class="hero">
    <div class="hero-photo" role="img" aria-label="Photo of two chrome swivel casters with blue polyurethane wheels"></div>
    <p class="hero-eyebrow">SOLUTIONS FOR <span class="rule"></span></p>
    <h1 class="hero-title">ALL YOUR<br>APPLICATIONS</h1>
    <div class="steps">
      <span class="steps-label">Easy as :</span>
      <div class="step-track"><span class="step">1</span><span class="step">2</span><span class="step">3</span></div>
    </div>
    <ul class="bullet-list">
      <li><svg><use href="#i-arrow-circle"/></svg>Request a Quote</li>
      <li><svg><use href="#i-arrow-circle"/></svg>Receive a Quote</li>
      <li><svg><use href="#i-arrow-circle"/></svg>Convert a Quote to order</li>
    </ul>
    <span class="btn btn--quote">REQUEST A QUOTE <svg><use href="#i-arrow"/></svg></span>
    <span class="btn btn--catalog">CATALOG <svg viewBox="0 0 18 16"><use href="#i-book"/></svg></span>
  </div>

  <footer class="site-footer">
    <svg class="footer-shape" width="765" height="90" viewBox="0 0 765 90" aria-hidden="true">
      <polygon points="0,34 142,34 142,45 78,45 60,22 0,22" fill="#55595e"/>
      <polygon points="765,34 623,34 623,45 687,45 705,22 765,22" fill="#55595e"/>
      <polygon points="0,11 64,11 82,34 683,34 701,11 765,11 765,90 0,90" fill="#3a3d42"/>
    </svg>
    <p class="copyright">Copyright © 2022 Pivots &amp; Treads All rights reserved.</p>
  </footer>

  <div class="dim"></div>

  <div class="quote-modal">
    <span class="modal-close">CLOSE <svg viewBox="0 0 10 10"><use href="#i-close"/></svg></span>
    <div class="quote-fields">
      <span class="field"><svg><use href="#i-user"/></svg>First Name</span>
      <span class="field"><svg><use href="#i-user"/></svg>Last Name</span>
      <span class="field"><svg><use href="#i-mail"/></svg>Email Address</span>
      <span class="field"><svg><use href="#i-question"/></svg>Optional Questions</span>
      <span class="field"><svg><use href="#i-briefcase"/></svg>Company Name</span>
      <span class="field"><svg><use href="#i-phone"/></svg>Best Contact Number</span>
    </div>
    <span class="btn btn--submit">SUBMIT <svg><use href="#i-arrow"/></svg></span>
  </div>
</section>

</body>
</html>
```